Velquor Medspa Home Page Design

I need a home page designed for a medical spa of which there are thousands in the US. Their primary purpose is to enhance personal beauty using non-surgical means, such as laser treatment and micro-needling. Since insurance typically doesn't cover such procedures, we are appealing to a mostly upscale end user, probably about 70% female.

Target Market(s)

Women 35-54

Industry/Entity Type

Medical cosmetics

Number of Pages Required

1 page

Font styles to use
Other font styles liked:
• I want very readable content, even by seniors. No grey copy, please. Black only.

Requirements
Must have
• This needs to be a photo-heavy design. Here's one example among hundreds to illustrate what other practices put forth to attract patients. https://www.plomerivaclinics.com/ Stock photos are fine, though I would prefer they obtained from Pixbarrow since I have an account with them. Finally, for now, I'm looking for a static website, we'll do the coding ourselves. Thank you. r psare
Nice to have
• I would also like you tpo consider staggering the five areas with content and a photo on the home page where the dominant photos are not always on the left or right. I think that help provide somefluidity to the sit's overall appearance. And "smooth" is a key quality as, in mamy cases, that's what attracts patients, i.e., the promise of smoother looking skin. his style: four e
Should not have
• Nice, open layout, but not loose. The home page document I attached contains all home page content and everything you need for the navigation bar.

```html
<!DOCTYPE html>
<html lang="en">
<head>
<meta charset="utf-8">
<title>Velquor Medspa — Home</title>
<link href="https://fonts.googleapis.com/css2?family=Libre+Baskerville:wght@400;700&family=Mulish:wght@400;600;700&display=swap" rel="stylesheet">
<style>
:root{
  --plum:#9a4a78;
  --plum-dark:#3b1a2b;
  --olive:#8b8a2f;
  --ink:#1a1a1a;
  --line:#d6d6d6;
  --menu:#e6e9ef;
  --field:#eef0f5;
  --white:#ffffff;
}
*{box-sizing:border-box;margin:0;padding:0}
html,body{width:1200px;height:3977px;overflow:hidden;background:var(--white)}
body{position:relative;font-family:"Mulish",sans-serif;color:var(--ink)}
.abs{position:absolute}
.wordmark{font-family:"Mulish",sans-serif;font-weight:700;color:var(--plum);letter-spacing:1px}
.site-header{left:141px;top:0;width:907px;height:77px;border-bottom:1px solid var(--line)}
.site-header .wordmark{position:absolute;left:50px;top:20px;font-size:28px}
.main-nav{position:absolute;left:360px;top:36px;display:flex;gap:22px;font-size:9px;letter-spacing:.5px}
.header-phone{position:absolute;right:50px;top:32px;font-size:16px;color:var(--plum);font-family:"Libre Baskerville",serif}
.header-phone b{font-family:"Mulish",sans-serif;font-size:13px;font-weight:700}
.dropdown{background:var(--menu);font-size:8px;letter-spacing:.4px}
.dropdown li{list-style:none;height:25px;line-height:25px;padding-left:12px}
.dropdown li.active{background:var(--plum);color:var(--white)}
.hero-title{left:196px;top:130px;font-family:"Libre Baskerville",serif;font-size:39px;line-height:56px;color:var(--ink)}
.hero-title .accent{color:var(--olive);font-weight:700}
.section-heading{font-size:16px;letter-spacing:2.5px;font-weight:600}
.copy{font-size:11px;line-height:16px;color:var(--ink)}
.btn{display:inline-block;border:2px solid var(--olive);border-radius:20px;font-size:10px;letter-spacing:1.5px;text-align:center;color:var(--ink)}
.field{background:var(--field);border:1px solid #e0e3ea;font-size:9px;color:#555;padding:7px 9px;height:28px}
.footer{left:141px;top:3702px;width:907px;height:210px;background:var(--plum-dark);color:#d9b7c7;font-size:9px}
.footer h4{font-weight:400;font-size:10px;letter-spacing:.5px;margin-bottom:14px;color:#e6cbd8}
.footer li{list-style:none;line-height:18px}
</style>
</head>
<body>

<header class="abs site-header">
  <div class="wordmark">Velquor Medspa</div>
  <nav class="main-nav"><span>TREATMENTS</span><span>ABOUT US</span><span>CONTACT</span></nav>
  <div class="header-phone">phone <b>| 555-214-0398</b></div>
</header>

<div class="abs hero-photo" style="left:612px;top:78px;width:436px;height:488px">
  <svg width="436" height="488" viewBox="0 0 436 488" role="img" aria-label="Spa still life with candles, bath salts in a wooden bowl, rolled white towels and pink blossoms">
    <defs><linearGradient id="heroG" x1="0" y1="0" x2="1" y2="1"><stop offset="0" stop-color="#6b4538"/><stop offset=".55" stop-color="#9c7763"/><stop offset="1" stop-color="#3e2a22"/></linearGradient></defs>
    <path d="M40 0H436V488H14C-8 380-6 120 40 0Z" fill="url(#heroG)"/>
    <path d="M40 0C-6 120-8 380 14 488" fill="none" stroke="var(--plum)" stroke-width="4"/>
  </svg>
</div>

<ul class="abs dropdown" style="left:488px;top:54px;width:149px">
  <li>INJECTABLES</li><li class="active">LASER TREATMENTS</li><li>MICRONEEDLING</li><li>OTHER TREATMENTS</li>
</ul>
<ul class="abs dropdown" style="left:637px;top:79px;width:150px">
  <li>HAIR REMOVAL</li><li>TATTOO REMOVAL</li><li>FACIAL REJUVENATION</li><li>SKIN RESURFACING</li><li>SCAR TREATMENT</li><li>STRETCH MARKS</li><li>OTHER LASER TREATMENTS</li>
</ul>

<h1 class="abs hero-title">THE<br>NON-SURGICAL<br>APPROACH TO A<br><span class="accent">CONFIDENT</span> YOU</h1>

<section class="abs about" style="left:184px;top:614px;width:810px">
  <h2 class="section-heading">ABOUT US</h2>
  <p class="copy" style="margin-top:12px;font-size:10px">Established by Dr. Anil Mehra, M.D., F.A.C.S., Velquor Medspa employs the latest in nonsurgical cosmetic innovations to enhance your appearance and the way you feel about yourself. All Velquor procedures are non-surgical as we effect healthier, younger-looking skin, facial reshaping, scar and hair removal numerous other results. Have concerns? Contact us now so we can help put your mind at ease. That's the essence of Velquor.</p>
  <span class="btn" style="margin-top:10px;width:127px;height:25px;line-height:21px;font-size:7px">LEARN MORE</span>
</section>

<!-- Treatment 1 -->
<div class="abs" style="left:141px;top:788px">
  <svg width="390" height="487" role="img" aria-label="Portrait of a woman with long blonde hair holding a syringe for injectables">
    <defs><linearGradient id="g1" x1="0" y1="0" x2="1" y2="1"><stop offset="0" stop-color="#e7ddd4"/><stop offset="1" stop-color="#c9a88a"/></linearGradient></defs>
    <path d="M0 0H300C390 110 400 380 330 487H0Z" fill="url(#g1)"/>
    <path d="M300 0C390 110 400 380 330 487" fill="none" stroke="var(--olive)" stroke-width="3"/>
  </svg>
</div>
<section class="abs" style="left:566px;top:950px;width:440px">
  <h2 class="section-heading">INJECTABLES</h2>
  <p class="copy" style="margin-top:28px">Injectables (also known as derma fillers) are gel-like substances we use to restore lost volume, smooth out wrinkles, and eliminate or soften facial lines. More than one million men and women per year seek injectable treatments to smooth out their chins, enhance or restore volume to sagging cheeks, or plump up their lips. Injectables also can help improve facial symmetry.</p>
  <span class="btn" style="margin-top:18px;width:122px;height:32px;line-height:28px">READ MORE</span>
</section>

<!-- Treatment 2 -->
<section class="abs" style="left:188px;top:1439px;width:434px;text-align:right">
  <h2 class="section-heading">LASER TREATMENTS</h2>
  <p class="copy" style="margin-top:28px;text-align:left">Velquor Medspa offers numerous laser-based treatments to enhance your personal appearance and boost your self-confidence. We have the right laser treatment option to remove hair and tattoos, tighten your skin, reduce stretch marks, and eliminate blemishes red spots. Plagued by rosacea, acne scars, or even keloids? We have the right treatment plan for you, too.</p>
  <span class="btn" style="margin-top:18px;width:122px;height:32px;line-height:28px">READ MORE</span>
</section>
<div class="abs" style="left:658px;top:1275px">
  <svg width="390" height="490" role="img" aria-label="Woman relaxing with eyes closed during a facial laser treatment">
    <defs><linearGradient id="g2" x1="0" y1="0" x2="1" y2="1"><stop offset="0" stop-color="#d9c3b3"/><stop offset="1" stop-color="#a88672"/></linearGradient></defs>
    <path d="M80 0H390V490H60C-10 380-10 110 80 0Z" fill="url(#g2)"/>
    <path d="M80 0C-10 110-10 380 60 490" fill="none" stroke="var(--olive)" stroke-width="3"/>
  </svg>
</div>

<!-- Treatment 3 -->
<div class="abs" style="left:141px;top:1765px">
  <svg width="390" height="489" role="img" aria-label="Close-up of a woman's face with hexagon overlays showing skin texture">
    <defs><linearGradient id="g3" x1="0" y1="0" x2="1" y2="1"><stop offset="0" stop-color="#e8e4df"/><stop offset="1" stop-color="#c7a999"/></linearGradient></defs>
    <path d="M0 0H300C390 110 400 380 330 489H0Z" fill="url(#g3)"/>
    <path d="M300 0C390 110 400 380 330 489" fill="none" stroke="var(--olive)" stroke-width="3"/>
  </svg>
</div>
<section class="abs" style="left:566px;top:1936px;width:440px">
  <h2 class="section-heading">MICRO-NEEDLING WITH PRP</h2>
  <p class="copy" style="margin-top:28px">Microneedling is a proven effective means to induce the regrowth of collagen. As we age, collagen production naturally declines, thus contributing to skin wrinkling and sagging. Velquor can help reverse that trend with microneedling and PRP (platelet rich plasma) injections combined.</p>
  <span class="btn" style="margin-top:18px;width:122px;height:32px;line-height:28px">READ MORE</span>
</section>

<!-- Treatment 4 -->
<section class="abs" style="left:188px;top:2428px;width:434px;text-align:right">
  <h2 class="section-heading">OTHER TREATMENT OPTIONS</h2>
  <p class="copy" style="margin-top:28px;text-align:left">Using a process called chemical peeling, Velquor can remove the top layers of skin so healthier looking skin can grow back in its place. A chemical peel is an effective and popular way to treat wrinkles, and scars. Many patients also find a chemical peel the ideal solution to repair sun damage and address other skin issues</p>
  <span class="btn" style="margin-top:18px;width:122px;height:32px;line-height:28px">READ MORE</span>
</section>
<div class="abs" style="left:658px;top:2254px">
  <svg width="390" height="488" role="img" aria-label="Woman receiving a chemical peel mask facial treatment">
    <defs><linearGradient id="g4" x1="0" y1="0" x2="1" y2="1"><stop offset="0" stop-color="#e6d6c8"/><stop offset="1" stop-color="#b99580"/></linearGradient></defs>
    <path d="M80 0H390V488H60C-10 380-10 110 80 0Z" fill="url(#g4)"/>
    <path d="M80 0C-10 110-10 380 60 488" fill="none" stroke="var(--olive)" stroke-width="3"/>
  </svg>
</div>

<!-- Consultation -->
<section class="abs consultation" style="left:265px;top:2808px;width:660px">
  <h2 style="text-align:center;font-size:12px;letter-spacing:2px;font-weight:400">SCHEDULE YOUR FREE CONSULTATION</h2>
  <p class="copy" style="margin-top:14px;font-size:10px">Why wonder if you're a candidate for our services when you can so easily find out for yourself? Simply complete and submit this form and a member of our medical team will contact you to schedule your visit. We'll listen to your concerns, answer your questions, and recommend the best strategy for improving how you look and feel about yourself. That's the Velquor way.</p>
</section>
<form class="abs consult-form" style="left:265px;top:2918px;width:660px;height:170px">
  <div class="abs field" style="left:0;top:0;width:324px">First Name *</div>
  <div class="abs field" style="left:336px;top:0;width:324px">Last Name *</div>
  <div class="abs field" style="left:0;top:36px;width:324px">Phone *</div>
  <div class="abs field" style="left:336px;top:36px;width:324px">Email *</div>
  <div class="abs field" style="left:0;top:72px;width:324px">City *</div>
  <div class="abs field" style="left:336px;top:72px;width:324px">How did you hear about Velquor ?
    <svg class="abs" style="right:10px;top:11px" width="9" height="6"><path d="M1 1l3.5 3.5L8 1" fill="none" stroke="#555" stroke-width="1.2"/></svg></div>
  <div class="abs field" style="left:0;top:108px;width:324px;height:56px">Message</div>
</form>
<div class="abs" style="left:424px;top:3103px;font-size:8px;display:flex;align-items:center;gap:6px">
  <span style="width:10px;height:10px;border:1px solid #777;display:inline-block"></span>I accept the Terms of Use &amp; agree to receive monthly specials, newsletters, etc. *
</div>
<span class="abs btn" style="left:498px;top:3163px;width:194px;height:34px;line-height:30px">BOOK AN APPOINTMENT</span>

<!-- Contact block -->
<div class="abs wordmark" style="left:0;width:1200px;top:3256px;text-align:center;font-size:64px;letter-spacing:3px">Velquor Medspa</div>
<address class="abs" style="left:0;width:1200px;top:3390px;text-align:center;font-style:normal;font-size:11px;line-height:21px">418 Marlow Avenue<br>Ashford CT 06000</address>
<div class="abs" style="left:0;width:1200px;top:3434px;text-align:center;font-size:30px;font-weight:600;letter-spacing:1px">555-214-0398</div>

<div class="abs" style="left:141px;top:3544px;width:907px;height:158px;background:linear-gradient(120deg,#bfe3c9,#a9d6b7 60%,#c5e6cf)" role="img" aria-label="Map showing the clinic location">
  <svg class="abs" style="left:447px;top:64px" width="14" height="20"><path d="M7 19C3 13 1 10 1 7a6 6 0 0112 0c0 3-2 6-6 12z" fill="#d93a2e"/><circle cx="7" cy="7" r="2.2" fill="#7a1a14"/></svg>
</div>

<footer class="abs footer">
  <div class="abs" style="left:150px;top:28px"><h4>INJECTABLES</h4><ul><li>Neuromodulator</li><li>Dermal Filler</li><li>Jawline Contour</li></ul></div>
  <div class="abs" style="left:406px;top:28px"><h4>LASER TREATMENTS</h4><ul><li>Hair Removal</li><li>Tattoo Removal</li><li>Facial Rejuvenation</li><li>Skin Resurfacing</li><li>Scar Treatment</li><li>Stretch Marks</li><li>Other Laser Treatments</li></ul></div>
  <div class="abs" style="left:658px;top:28px"><h4>OTHER TREATMENT OPTIONS</h4><ul><li>Chemical Peels</li><li>Intense Pulsed Light (IPL) Therapy</li></ul>
    <ul style="margin-top:22px;text-align:center;width:140px"><li>ABOUT US</li><li style="margin-top:6px">CONTACT</li></ul></div>
</footer>
<div class="abs" style="left:0;width:1200px;top:3921px;text-align:center;font-size:8px;color:var(--plum)">2023 © copyright</div>

</body>
</html>
```